Rising Harbor Glow Gala Graphic Design

I’m seeking a professional graphic designer experienced in event branding to create a cohesive suite of materials for our third annual fundraising gala, “Rising Harbor Glow.” This year's theme is " An Evening in Silver for Rising Harbor Glow" Need to design collateral for website, social media and email blasts.
Target Market(s)
Affluent gala attendees
Industry/Entity Type
Fundraising / Charity / Outdoors / Sports
Font styles to use
Decorative
Script
Colors
0054AA
0677BA
7BADD7
CADEEF
E8F1F8
0094D4
00A9DD
6FCCEA
C7EBF8
E9F6FB
00AB8E
00BBA5
67D7C9
C6EFE9
E9F9F6
6B429C
8869AF
B7A5CE
E3DAEB
F3F0F8

```html
<!DOCTYPE html>
<html lang="en">
<head>
<meta charset="UTF-8">
<title>Rising Harbor Glow – Social Media</title>
<link rel="stylesheet" href="https://fonts.googleapis.com/css2?family=Oswald:wght@300;400;500&family=Noto+Serif:wght@400;500&family=Poppins:wght@400;500&display=swap">
<style>
  :root{
    --page:#ffffff;
    --ink:#111111;
    --night:#06141d;
    --deep:#082a3c;
    --band:#0a2a3d;
    --footer:#04121b;
    --glow:#00a9dd;
    --glow-soft:#6fccea;
    --silver-hi:#ffffff;
    --silver-mid:#c9ced3;
    --silver-lo:#8e959b;
    --line:#d9dde0;
    --text:#f2f4f6;
  }
  *{margin:0;padding:0;box-sizing:border-box}
  html,body{width:1117px;height:1200px;overflow:hidden;background:var(--page)}
  .sheet{position:relative;width:1117px;height:1200px}
  .sheet-label{
    position:absolute;top:38px;left:0;width:100%;text-align:center;
    font-family:"Poppins",sans-serif;font-weight:400;font-size:56px;letter-spacing:5px;color:var(--ink);line-height:1;
  }
  .poster{
    position:absolute;left:65px;top:128px;width:980px;height:980px;overflow:hidden;
    background:var(--night);
  }
  .poster-stage{
    position:absolute;left:0;top:267px;width:980px;height:509px;
    background:
      radial-gradient(ellipse 180px 300px at 490px 200px, rgba(0,169,221,.55), rgba(0,169,221,0) 100%),
      radial-gradient(ellipse 420px 420px at 490px 120px, rgba(0,148,212,.45), rgba(0,148,212,0) 100%),
      linear-gradient(180deg,#0a3144 0%,#0a3a52 45%,#093347 100%);
  }
  .poster-flare{
    position:absolute;left:390px;top:220px;width:200px;height:90px;
    background:radial-gradient(ellipse 100px 30px at 100px 45px, rgba(200,240,255,.95), rgba(0,169,221,.5) 30%, rgba(0,169,221,0) 100%);
  }
  .frame-line{position:absolute;background:var(--line)}
  .frame-left-a{left:15px;top:37px;width:1.5px;height:739px}
  .frame-left-b{left:32px;top:32px;width:1.5px;height:744px}
  .frame-top-a{left:15px;top:37px;width:900px;height:1.5px;background:linear-gradient(90deg,var(--line),rgba(217,221,224,0))}
  .frame-top-b{left:32px;top:32px;width:880px;height:1.5px;background:linear-gradient(90deg,var(--line),rgba(217,221,224,0))}
  .frame-right-a{left:931px;top:100px;width:1.5px;height:676px;background:linear-gradient(180deg,rgba(217,221,224,0),var(--line) 20%)}
  .frame-right-b{left:948px;top:110px;width:1.5px;height:666px;background:linear-gradient(180deg,rgba(217,221,224,0),var(--line) 20%)}

  .rule{position:absolute;height:1.5px}
  .rule-fade{background:linear-gradient(90deg,rgba(217,221,224,0),var(--line) 50%,rgba(217,221,224,0))}

  .invite{
    position:absolute;top:78px;left:0;width:980px;text-align:center;
    font-family:"Noto Serif",serif;font-size:27px;letter-spacing:5px;color:var(--text);line-height:1.1;
  }
  .silver{
    background:linear-gradient(180deg,var(--silver-hi) 0%,var(--silver-hi) 35%,var(--silver-lo) 50%,var(--silver-hi) 65%,var(--silver-mid) 100%);
    -webkit-background-clip:text;background-clip:text;color:transparent;
  }
  .theme-title{
    position:absolute;top:118px;left:0;width:980px;text-align:center;
    font-family:"Oswald",sans-serif;font-weight:400;font-size:92px;line-height:1;letter-spacing:1px;white-space:nowrap;
  }
  .theme-title .small{font-size:40px}
  .gala-name{position:absolute;left:0;width:980px;text-align:center;font-family:"Oswald",sans-serif;font-weight:400;line-height:1;white-space:nowrap}
  .gala-name-top{top:292px;font-size:150px;letter-spacing:2px}
  .gala-name-bottom{top:434px;font-size:170px;letter-spacing:2px}
  .gala-name-bottom .small{font-size:52px;letter-spacing:0;margin-right:10px}
  .subtitle{
    position:absolute;top:632px;left:0;width:980px;text-align:center;
    font-family:"Noto Serif",serif;font-size:28px;letter-spacing:4px;color:var(--text);line-height:1;
  }
  .celebration{
    position:absolute;top:690px;left:0;width:980px;text-align:center;
    font-family:"Noto Serif",serif;font-size:20px;letter-spacing:3.5px;color:var(--text);line-height:28px;
  }
  .details{position:absolute;left:0;top:776px;width:980px;height:131px;background:var(--band)}
  .date-day{position:absolute;left:132px;top:17px;font-family:"Oswald",sans-serif;font-weight:400;font-size:92px;line-height:1;color:#fff;letter-spacing:-2px}
  .date-month{position:absolute;left:144px;top:98px;font-family:"Oswald",sans-serif;font-weight:300;font-size:18px;color:#fff;letter-spacing:.5px}
  .details-divider{position:absolute;left:302px;top:25px;width:1.5px;height:91px;background:var(--line)}
  .detail-row{position:absolute;left:322px;display:flex;align-items:center;gap:9px;font-family:"Oswald",sans-serif;font-weight:300;font-size:23px;color:#fff;letter-spacing:1px;white-space:nowrap}
  .detail-row svg{width:18px;height:18px;flex:none}
  .row-time{top:18px}.row-place{top:54px}.row-dress{top:91px}
  .footer{position:absolute;left:0;top:907px;width:980px;height:73px;background:var(--footer);display:flex;align-items:center;justify-content:center;gap:10px}
  .footer svg{width:18px;height:18px}
  .footer-url{font-family:"Poppins",sans-serif;font-weight:500;font-size:24px;letter-spacing:2px;color:#fff}
</style>
</head>
<body>
<div class="sheet">
  <div class="sheet-label">SOCIAL MEDIA</div>

  <section class="poster">
    <div class="poster-stage"></div>
    <div class="poster-flare"></div>

    <div class="frame-line frame-left-a"></div>
    <div class="frame-line frame-left-b"></div>
    <div class="frame-line frame-top-a"></div>
    <div class="frame-line frame-top-b"></div>
    <div class="frame-line frame-right-a"></div>
    <div class="frame-line frame-right-b"></div>

    <div class="rule" style="left:130px;top:91px;width:155px;background:linear-gradient(90deg,rgba(217,221,224,0),var(--line))"></div>
    <div class="rule" style="left:675px;top:91px;width:155px;background:linear-gradient(90deg,var(--line),rgba(217,221,224,0))"></div>
    <div class="invite">YOU ARE INVITED TO</div>

    <div class="theme-title"><span class="silver">AN EVENING <span class="small">IN</span> SILVER</span></div>

    <div class="rule rule-fade" style="left:130px;top:254px;width:720px"></div>
    <div class="rule rule-fade" style="left:130px;top:266px;width:720px;background:linear-gradient(90deg,rgba(217,221,224,0),#e6f6fb 50%,rgba(217,221,224,0))"></div>

    <div class="gala-name gala-name-top"><span class="silver">RISING</span></div>
    <div class="gala-name gala-name-bottom"><span class="silver"><span class="small">HARBOR</span>GLOW</span></div>

    <div class="rule rule-fade" style="left:260px;top:622px;width:460px"></div>
    <div class="subtitle">A FUNDRAISING GALA</div>
    <div class="rule rule-fade" style="left:260px;top:675px;width:460px"></div>

    <div class="celebration">IN CELEBRATION OF THE 150TH ANNIVERSARY<br>OF BEACON SHOAL LIGHTHOUSE</div>

    <div class="details">
      <div class="date-day">18TH</div>
      <div class="date-month">NOVEMBER ,2025</div>
      <div class="details-divider"></div>
      <div class="detail-row row-time">
        <svg viewBox="0 0 20 20"><circle cx="10" cy="10" r="8.5" fill="#fff"/><path d="M10 5v5.5l3.5 2" stroke="#0a2a3d" stroke-width="2" fill="none" stroke-linecap="round"/></svg>
        <span>COCTAILS 6:PM VIP TICKET HOLDRS 5:00PM</span>
      </div>
      <div class="detail-row row-place">
        <svg viewBox="0 0 20 20"><path d="M10 1.5a6 6 0 0 0-6 6c0 4.5 6 11 6 11s6-6.5 6-11a6 6 0 0 0-6-6z" fill="#fff"/><circle cx="10" cy="7.5" r="2.3" fill="#0a2a3d"/></svg>
        <span>CORAL POINT KEY-4120 SEASIDE HWY - MARLOW BAY</span>
      </div>
      <div class="detail-row row-dress">
        <svg viewBox="0 0 20 20"><path d="M2 3l8 15 8-15-4 1-4 3-4-3z" fill="#fff"/><path d="M8 6l2 1.5L12 6v3l-2-1.5L8 9z" fill="#0a2a3d"/></svg>
        <span>COCKTAIL ATTIRE - SPACE IS LIMITED</span>
      </div>
    </div>

    <footer class="footer">
      <svg viewBox="0 0 20 20" fill="none" stroke="#fff" stroke-width="1.6"><circle cx="10" cy="10" r="8"/><ellipse cx="10" cy="10" rx="3.5" ry="8"/><path d="M2 10h16M3.5 6h13M3.5 14h13"/></svg>
      <span class="footer-url">www.savebeaconshoallight.org</span>
    </footer>
  </section>
</div>
</body>
</html>
```